Fresh Dwelling Tract Hub needs a new Landing Page

I like to get a landing page or website with 2-3 pages to help target home buyers who are looking to buy homes from builders such as TQ Estates, Vostrum, P.J. Calloway, etc. The landing page/website to be non-cluttered and be able to explain to home buyers that there are many benefits to include me as their buyer's agent when they buy a brand new home from any builders.
I may want to incorporate a short explanation video (animated) on the landing page and then for the viewer to click on a button that will take them to another page where they can search for new homes from different builders.
Target Market(s)
Home buyers looking to buy brand new home from builders such as TQ Estates, Vostrum, P.J. Calloway, etc.
Industry/Entity Type
Real Estate
Number of Pages Required
2 page
Requirements
Must have
- The landing page may have the explanation video at the bottom of the landing page (scrolled down) or there may be a CALL TO ACTION button that takes the viewer to the 2nd page to watch the explanation video. Once they watched the explanation video and are still interested, they can click on another CALL TO ACTION button that will take them to another website that they will be able to search for all the available new homes and register their contact information.
Should not have
- No clutters and no dark colors.

```html
<!DOCTYPE html>
<html lang="en">
<head>
<meta charset="utf-8">
<title>Fresh Dwelling Tract Hub – New Home Buyer's Agent</title>
<link href="https://fonts.googleapis.com/css2?family=Open+Sans:wght@400;600;700&family=Raleway:wght@400;500;600&display=swap" rel="stylesheet">
<style>
:root{
  --ink:#222;
  --muted:#777;
  --accent:#e0895a;
  --headline:#d2262b;
  --band:#f0f0f0;
  --footer:#262626;
  --white:#fff;
}
*{box-sizing:border-box;margin:0;padding:0}
html,body{width:1200px;height:4839px;overflow:hidden}
body{position:relative;background:var(--white);font-family:"Open Sans",Arial,sans-serif;color:var(--ink)}
.abs{position:absolute}

.nav{left:0;top:0;width:1200px;height:97px;background:var(--white)}
.brand{left:200px;top:28px;font-family:"Raleway",sans-serif;font-size:24px;font-weight:500;color:var(--ink);white-space:nowrap}
.menu{right:203px;top:38px;display:flex;gap:30px;font-size:13px;letter-spacing:1px;text-transform:uppercase;font-weight:600}
.menu .active{color:#aaa}

.hero{left:0;top:97px;width:1200px;height:600px;background:linear-gradient(180deg,#3f8fd6 0%,#8cc1e8 30%,#4d7f94 48%,#5b7a3d 70%,#6d5a44 100%)}
.hero-kicker{left:0;top:180px;width:1200px;text-align:center;color:var(--white);font-size:13px;letter-spacing:2px}
.hero-title{left:0;top:220px;width:1200px;text-align:center;color:var(--headline);font-family:"Raleway",sans-serif;font-size:46px;font-weight:500;line-height:56px}
.hero-text{left:330px;top:335px;width:640px;text-align:center;color:var(--white);font-size:14px;line-height:20px}
.btn{background:var(--accent);color:var(--white);font-size:13px;font-weight:700;letter-spacing:1px;text-transform:uppercase;border-radius:24px;text-align:center;line-height:42px;height:42px;white-space:nowrap}
.hero-btn{left:496px;top:428px;width:208px}

.section-title{left:0;width:1200px;text-align:center;font-family:"Raleway",sans-serif;font-size:30px;font-weight:500}
.rule{left:585px;width:30px;height:1px;background:#bbb}
.fill{border-radius:2px}
.tile-label{text-align:center;color:var(--white);font-family:"Raleway",sans-serif;font-size:28px}

.video-title{left:203px;top:1092px;width:591px;text-align:center;color:var(--white);font-family:"Raleway",sans-serif;font-size:27px;text-transform:uppercase;letter-spacing:.5px}
.video-price{left:203px;top:1132px;width:591px;text-align:center;color:var(--white);font-family:"Open Sans",sans-serif;font-size:44px;font-weight:700}
.player{left:203px;top:1192px;width:591px;height:34px;background:rgba(0,0,0,.55)}
.player-time{left:260px;top:1201px;color:var(--white);font-size:11px}

.banner{left:0;top:1626px;width:1200px;height:697px;background:linear-gradient(180deg,#6b7f9c 0%,#b9c3d3 38%,#8a8f93 60%,#4a4f57 100%)}
.banner-title{left:360px;top:1858px;color:var(--white);font-family:"Raleway",sans-serif;font-size:62px;line-height:76px}
.banner-btn{left:203px;top:2070px;width:210px}
.banner-text{left:432px;top:2150px;width:380px;color:var(--white);font-size:13px;line-height:18px}

.card{background:#222;color:var(--white);text-align:center}
.card .ph{height:158px}
.card .kick{font-size:10px;letter-spacing:1px;margin-top:14px;color:#ccc}
.card h3{font-family:"Raleway",sans-serif;font-size:24px;font-weight:500;margin:6px 0 12px}
.card .ln{width:30px;height:1px;background:#888;margin:0 auto 12px}
.card p{font-size:12px;line-height:16px;padding:0 20px;color:#ddd}
.card.hot{background:var(--accent)}
.card.hot .kick,.card.hot p{color:var(--white)}
.card.hot .ln{background:var(--white)}

.band{left:0;top:2829px;width:1200px;height:1494px;background:var(--band)}
.post{background:var(--white)}
.post .body{padding:16px 22px}
.post h4{font-family:"Raleway",sans-serif;font-size:20px;font-weight:500;margin-bottom:10px;white-space:nowrap}
.post h4.lead{color:var(--accent)}
.post h4.small{font-size:14px}
.post p{font-size:13px;line-height:17px;color:#555}
.post .meta{font-size:10px;letter-spacing:1px;color:#999;margin-top:12px}

.insta{top:4484px;width:187px;height:187px}
.footer{left:0;top:4758px;width:1200px;height:81px;background:var(--footer);color:#ccc;font-size:12px}
.footer .copy{left:200px;top:32px}
.footer .links{right:203px;top:32px}
</style>
</head>
<body>

<header class="abs nav">
  <div class="abs brand">Fresh Dwelling Tract Hub</div>
  <nav class="abs menu"><span class="active">Home</span><span>About</span><span>Builders</span><span>Video</span><span>Contact</span></nav>
</header>

<section class="abs hero" role="img" aria-label="Lakeside new home among gardens with mountains behind"></section>
<div class="abs hero-kicker">NEW HOME BUYERS</div>
<h1 class="abs hero-title">Buy New With Your Own Agent</h1>
<p class="abs hero-text">Buying a brand new home from a builder? Add me as your buyer's agent at no extra cost and get expert guidance from contract to closing.</p>
<div class="abs btn hero-btn">Find New Homes</div>

<h2 class="abs section-title" style="top:732px">Featured Builders</h2>
<div class="abs rule" style="top:794px"></div>

<div class="abs fill" style="left:203px;top:835px;width:591px;height:391px;background:linear-gradient(160deg,#3a1c14,#b0562a 55%,#1c2030)" role="img" aria-label="Explainer video still of a lit new home at night"></div>
<div class="abs video-title">Why Use A Buyer's Agent?</div>
<div class="abs video-price">$0 Cost To You</div>
<div class="abs player"></div>
<svg class="abs" style="left:214px;top:1201px" width="40" height="16" viewBox="0 0 40 16">
  <polygon points="0,2 0,14 10,8" fill="#fff"/>
  <rect x="18" y="3" width="3" height="10" fill="#fff"/><rect x="24" y="3" width="3" height="10" fill="#fff"/>
</svg>
<div class="abs player-time">0:24 / 1:30</div>
<svg class="abs" style="left:330px;top:1206px" width="380" height="6" viewBox="0 0 380 6">
  <rect width="380" height="4" y="1" fill="#777"/><rect width="90" height="4" y="1" fill="#d2262b"/>
</svg>

<div class="abs fill" style="left:806px;top:835px;width:191px;height:188px;background:radial-gradient(circle,#d6efd0,#ffffff 70%)" role="img" aria-label="Green house illustration"></div>
<div class="abs fill" style="left:806px;top:1035px;width:191px;height:191px;background:linear-gradient(180deg,#2a6fc4,#8ec3ea 60%,#1d4f8a)" role="img" aria-label="Rising market chart over blue sky"></div>
<div class="abs fill" style="left:203px;top:1239px;width:391px;height:313px;background:linear-gradient(180deg,#b7c8dc,#e8eef4 50%,#7b8da3)" role="img" aria-label="White modern builder home reflected in water"></div>
<div class="abs tile-label" style="left:203px;top:1350px;width:391px">TQ Estates</div>
<div class="abs fill" style="left:619px;top:1239px;width:378px;height:313px;background:linear-gradient(180deg,#6d5a3d,#d9a75a 45%,#2f8fd0)" role="img" aria-label="New community terrace with a blue pool"></div>
<div class="abs tile-label" style="left:619px;top:1350px;width:378px">Vostrum</div>

<section class="abs banner" role="img" aria-label="Modern new-build villa at dusk with reflecting pool"></section>
<h2 class="abs banner-title">Search Builders</h2>
<div class="abs btn banner-btn">Start Your Search</div>
<p class="abs banner-text">Browse every available new home from TQ Estates, Vostrum, P.J. Calloway and more, then register your details.</p>

<div class="abs card" style="left:203px;top:2400px;width:252px;height:316px">
  <div class="ph" role="img" aria-label="Houses with map pins" style="background:linear-gradient(180deg,#2d6fb0,#c0563a)"></div>
  <div class="kick">BENEFIT</div><h3>Free to You</h3><div class="ln"></div>
  <p>Builders pay my commission, so expert help costs you nothing.</p>
</div>
<div class="abs card" style="left:474px;top:2400px;width:252px;height:316px">
  <div class="ph" role="img" aria-label="Coin stacks with sprouts" style="background:linear-gradient(180deg,#1f3e63,#8a6a2c)"></div>
  <div class="kick">BENEFIT</div><h3>Smart Deals</h3><div class="ln"></div>
  <p>I review contracts, upgrades and incentives to protect your money.</p>
</div>
<div class="abs card hot" style="left:742px;top:2400px;width:255px;height:316px">
  <div class="ph" role="img" aria-label="Small house on green grass" style="background:linear-gradient(180deg,#cfe6a0,#4e9a2e)"></div>
  <div class="kick">CONTACT</div><h3 style="font-size:18px">Work with me</h3><div class="ln"></div>
  <p>Register today and start your new home search.</p>
</div>

<section class="abs band"></section>
<h2 class="abs section-title" style="top:2916px">Latest Articles</h2>
<div class="abs rule" style="top:2978px"></div>

<article class="abs post" style="left:203px;top:3016px;width:252px;height:355px">
  <div style="height:203px;background:radial-gradient(circle,#e86a4a,#f5eee8 70%)" role="img" aria-label="Hands holding a small house model"></div>
  <div class="body"><h4>Agent Benefits</h4><p>What a buyer's agent does for you at a builder sale.</p><div class="meta">GUIDE - AUG 1, 2019</div></div>
</article>
<div class="abs" style="left:203px;top:3390px;width:252px;height:313px;background:linear-gradient(160deg,#fff,#f0c9a4)" role="img" aria-label="New home promotion with a hand holding a house"></div>
<article class="abs post" style="left:203px;top:3720px;width:252px;height:493px">
  <div style="height:340px;background:linear-gradient(180deg,#f0b060,#9a6a40 55%,#3a2a20)" role="img" aria-label="Patio lounge at sunset"></div>
  <div class="body"><h4>Closing Tips</h4><p>Steps to a smooth closing on your brand new home.</p><div class="meta">GUIDE - AUG 1, 2019</div></div>
</article>

<article class="abs post" style="left:474px;top:3016px;width:252px;height:284px">
  <div style="height:148px;background:linear-gradient(180deg,#2a6fc4,#8ec3ea 60%,#1d4f8a)" role="img" aria-label="Market chart over sky"></div>
  <div class="body"><h4>Market Update</h4><p>New home prices and builder incentives this season.</p><div class="meta">NEWS - AUG 1, 2019</div></div>
</article>
<article class="abs post" style="left:474px;top:3323px;width:252px;height:474px">
  <div style="height:330px;background:linear-gradient(180deg,#7fb5e0,#5e9a4a 55%,#c9d0d8)" role="img" aria-label="Waterfront new home with palm trees"></div>
  <div class="body"><h4 class="lead">Why Hire Me</h4><p>Bring me on your first visit to keep your rights.</p><div class="meta">GUIDE - AUG 1, 2019</div></div>
</article>
<article class="abs post" style="left:474px;top:3810px;width:252px;height:403px">
  <div style="height:250px;background:linear-gradient(180deg,#6c8fb8,#b9b2a5 55%,#4f7a3a)" role="img" aria-label="Two-storey suburban new home"></div>
  <div class="body"><h4 class="small">Model Homes</h4><p>How to tour model homes and compare builder options.</p></div>
</article>

<article class="abs post" style="left:742px;top:3016px;width:255px;height:439px">
  <div style="height:280px;background:linear-gradient(180deg,#8fc0e8,#d99a5a 55%,#5a4030)" role="img" aria-label="Outdoor patio with furniture"></div>
  <div class="body"><h4>Upgrade Guide</h4><p>Which builder upgrades add value and which to skip.</p><div class="meta">GUIDE - AUG 1, 2019</div></div>
</article>
<article class="abs post" style="left:742px;top:3471px;width:255px;height:439px">
  <div style="height:280px;background:linear-gradient(180deg,#a9c9e6,#7d7a6a 55%,#3d6b2e)" role="img" aria-label="Stately new home on a lawn"></div>
  <div class="body"><h4>Lot Selection</h4><p>Choosing the right lot in a new home community.</p><div class="meta">GUIDE - AUG 1, 2019</div></div>
</article>
<article class="abs post" style="left:742px;top:3936px;width:255px;height:277px">
  <div style="height:120px;background:radial-gradient(circle,#e88a6a,#f8f2ee 70%)" role="img" aria-label="Hands around a small house"></div>
  <div class="body"><h4>Contract Basics</h4><p>Read the builder contract before you sign it.</p><div class="meta">GUIDE - AUG 1, 2019</div></div>
</article>

<h2 class="abs section-title" style="top:4383px">Instagram</h2>
<div class="abs rule" style="top:4440px"></div>
<div class="abs insta" style="left:194px;background:linear-gradient(180deg,#1f3e63,#8a6a2c)" role="img" aria-label="Coin stacks with sprouts"></div>
<div class="abs insta" style="left:397px;background:linear-gradient(180deg,#c9d6e2,#6a6a5e)" role="img" aria-label="Street of new houses"></div>
<div class="abs insta" style="left:600px;background:linear-gradient(180deg,#e6eaef,#8a9bb0)" role="img" aria-label="Signing a home purchase contract"></div>
<div class="abs insta" style="left:803px;background:linear-gradient(180deg,#bcd4ea,#5d7a4a)" role="img" aria-label="New house with a for-sale sign"></div>

<footer class="abs footer">
  <div class="abs copy">Copyright 2019 Fresh Dwelling Tract Hub All Rights Reserved</div>
  <div class="abs links">PRIVACY POLICY &nbsp;|&nbsp; TERMS &amp; CONDITIONS</div>
</footer>

</body>
</html>
```